FRESH WEB DESIGN FOR A HEALTH - SOCIAL NETWORK

We are currently looking for a creative, fresh, vibrant, inspiring design for a new social network focused on health and nutrition for health professionals (namely nutritionists) and end-users.

Design requirements - IMPORTANT: please see attached file 'LumaCrest web site design scope' for the detailed brief.

The web site requires new design templates with inter-changeable banners and in some cases profile images. It's important for the website to communicate LumaCrest's core values and image which includes fun, vitality, freshness, life fulfillment, trust, integrity and loyalty to the two target groups. Imagery must have a consistent/inter-related theme across all communities, topics and resources, which need to be easily applied to the web site.To help engage our audience we are looking for something fresh and unique in the selected imagery/ theme/ design templates.

The chosen design will need to be applied to create a PDF, PowerPoint and business card template.

Please see attached file 'LumaCrest web site design scope' to view the LumaCrest web site, which is currently under development.

Nutrition

```html
<!DOCTYPE html>
<html lang="en">
<head>
<meta charset="utf-8">
<title>LumaCrest – Health Social Network</title>
<link href="https://fonts.googleapis.com/css2?family=Exo:wght@400;500;600&family=Open+Sans:ital,wght@0,400;0,600;1,400&display=swap" rel="stylesheet">
<style>
:root{
  --page-bg:#efefef;
  --white:#ffffff;
  --blue:#1a8fc9;
  --nav:#666666;
  --green:#8cc63f;
  --lime:#a5c422;
  --orange:#f7941d;
  --orange-mid:#f9a54a;
  --orange-light:#f9b46a;
  --grass:#3aa935;
  --sky:#29a8d8;
  --purple:#6a2d83;
  --text:#8a8a8a;
  --heading-gray:#777777;
  --line:#dddddd;
  --band:#eeeeee;
  --footer:#2d2d2d;
  --footer-bottom:#242424;
  --footer-text:#8d8d8d;
  --footer-head:#dddddd;
  --icon-bg:#e8e8e8;
  --icon-fg:#666666;
}
*{margin:0;padding:0;box-sizing:border-box}
h1,h2,h3,h4{font-weight:400}
html,body{width:1200px;height:2258px;overflow:hidden}
body{background:var(--page-bg);font-family:'Open Sans',sans-serif;color:var(--text);position:relative}
.page{position:absolute;left:99px;top:0;width:1001px;height:2258px;background:var(--white)}
.abs{position:absolute}

/* header */
.brand{left:12px;top:32px;display:flex;align-items:center;gap:12px}
.brand-mark{width:58px;height:58px;border-radius:50%;background:var(--green)}
.brand-name{font-family:'Exo',sans-serif;font-weight:600;font-size:48px;color:var(--green);letter-spacing:-0.5px}
.nav{right:10px;top:78px;display:flex;gap:35px;font-family:'Exo',sans-serif;font-size:16px;color:var(--nav);list-style:none}
.nav .active{color:var(--blue)}

/* hero */
.hero{left:0;top:134px;width:1001px;height:405px;background:linear-gradient(90deg,#7d858c 0%,#8c949a 40%,#9aa1a6 100%)}
.hero-photo{left:0;top:0;width:353px;height:405px;background:linear-gradient(180deg,#a4adb3,#6f8fb2 60%,#5e7fa6)}
.hero-title{left:200px;width:840px;top:68px;text-align:center;font-family:'Exo',sans-serif;font-size:37px;color:#fff;letter-spacing:0.5px}
.hero svg{position:absolute}

/* pillars */
.pillar{top:585px;width:140px;text-align:center}
.pillar .disc{width:92px;height:92px;border-radius:50%;background:var(--icon-bg);margin:0 auto;display:flex;align-items:center;justify-content:center}
.pillar .label{font-family:'Exo',sans-serif;font-size:19px;margin-top:17px}
.rule{height:1px;background:var(--line)}

/* mission */
.mission-photo{left:11px;top:801px;width:226px;height:155px;background:linear-gradient(135deg,#bdbdbd,#9c9c9c)}
.mission-title{left:252px;top:797px;font-family:'Exo',sans-serif;font-size:30px;color:var(--purple);font-weight:500}
.mission-text{left:252px;top:843px;width:432px;font-size:13.5px;line-height:23px;color:var(--text)}
.vline{width:1px;background:var(--line)}
.pill{left:708px;width:283px;height:48px;color:#fff;font-family:'Exo',sans-serif;font-size:21px;display:flex;align-items:center;padding-left:12px;gap:12px}

/* discussions */
.section-title{left:11px;top:1036px;font-family:'Exo',sans-serif;font-size:27px;color:var(--blue);font-weight:500}
.thumb{width:323px;height:157px}
.caption{font-family:'Exo',sans-serif;font-size:17px;color:#8a8a8a}
.cat-title{left:699px;top:1042px;font-family:'Exo',sans-serif;font-size:22px;color:var(--heading-gray)}
.cats{left:699px;top:1083px;width:292px;list-style:none}
.cats li{height:42.6px;border-top:1px solid var(--line);display:flex;align-items:center;padding-left:14px;font-family:'Exo',sans-serif;font-size:15.5px;color:#8a8a8a}
.cats li:last-child{border-bottom:1px solid var(--line)}
.cats li::before{content:"";width:5px;height:5px;border-radius:50%;background:#aaa;margin-right:10px}
.cats li.current{color:var(--blue)}
.cats li.current::before{background:var(--blue)}

/* testimonials */
.testi{left:0;top:1554px;width:1001px;height:260px;background:var(--band)}
.testi-title{left:0;width:1001px;top:30px;text-align:center;font-family:'Exo',sans-serif;font-size:21px;color:var(--heading-gray);letter-spacing:0.5px}
.avatar{left:26px;top:77px;width:126px;height:126px;border-radius:50%;border:5px solid #fff;background:linear-gradient(180deg,#e3e3e3,#c8c8c8);box-shadow:0 2px 6px rgba(0,0,0,.15)}
.quote{left:173px;top:88px;width:810px;font-style:italic;font-size:14.5px;line-height:25px;color:#8a8a8a}
.author{left:173px;top:167px;font-size:15px;color:var(--purple)}

/* signup */
.signup{left:0;top:1814px;width:1001px;height:101px;background:var(--orange)}
.signup-title{left:15px;top:35px;font-family:'Exo',sans-serif;font-size:24px;line-height:34px;color:#fff;white-space:nowrap}
.field{top:35px;height:34px;background:#fff;border-radius:3px;font-size:13px;color:#999;display:flex;align-items:center;padding-left:13px}
.btn{left:887px;top:35px;width:98px;height:34px;border-radius:3px;background:#3d3d3d;color:#fff;font-size:13px;display:flex;align-items:center;justify-content:center}

/* footer */
.footer{left:0;top:1915px;width:1001px;height:252px;background:var(--footer)}
.f-head{top:47px;font-family:'Exo',sans-serif;font-size:16px;color:var(--footer-head)}
.f-text{font-size:12px;line-height:22.6px;color:var(--footer-text)}
.f-more{font-size:12px;color:#cfcfcf}
.f-div{top:32px;width:1px;height:190px;background:#3e3e3e}
.f-links{list-style:none;font-size:12px;line-height:22.6px;color:var(--footer-text);top:78px}
.bottom{left:0;top:2167px;width:1001px;height:91px;background:var(--footer-bottom)}
.copy{left:14px;top:36px;font-size:12px;color:var(--footer-text)}
.social{top:28px;width:34px;height:34px;border-radius:50%;background:#5a5a5a}
</style>
</head>
<body>
<div class="page">

  <header>
    <div class="abs brand"><span class="brand-mark"></span><span class="brand-name">LumaCrest</span></div>
    <ul class="abs nav">
      <li class="active">HOME</li><li>ABOUT US</li><li>SERVICES</li><li>TESTIMONIALS</li><li>MEDIA</li><li>CONTACT US</li>
    </ul>
  </header>

  <section class="abs hero">
    <div class="abs hero-photo" role="img" aria-label="Smiling senior man in a blue shirt"></div>
    <h1 class="abs hero-title">TIRED OF HAVING NO ENERGY?</h1>
    <svg style="left:445px;top:146px" width="112" height="112" viewBox="0 0 112 112"><circle cx="56" cy="56" r="51" fill="none" stroke="#fff" stroke-width="7"/><path d="M42 32 L80 56 L42 80 Z" fill="#fff"/></svg>
    <svg style="left:20px;top:186px" width="20" height="30" viewBox="0 0 20 30"><path d="M16 2 L4 15 L16 28" fill="none" stroke="rgba(255,255,255,.5)" stroke-width="3"/></svg>
    <svg style="left:962px;top:186px" width="20" height="30" viewBox="0 0 20 30"><path d="M4 2 L16 15 L4 28" fill="none" stroke="rgba(255,255,255,.5)" stroke-width="3"/></svg>
  </section>

  <section class="pillars">
    <div class="abs pillar" style="left:24px"><div class="disc"><svg width="30" height="34" viewBox="0 0 30 34" fill="var(--icon-fg)"><rect x="5" y="2" width="2" height="10"/><rect x="9" y="2" width="2" height="10"/><rect x="13" y="2" width="2" height="10"/><rect x="8" y="10" width="4" height="22" rx="2"/><path d="M20 2 c6 2 6 12 2 14 v16 h-4 V2z"/></svg></div><div class="label" style="color:var(--lime)">NUTRITION</div></div>
    <div class="abs pillar" style="left:227px"><div class="disc"><svg width="30" height="30" viewBox="0 0 30 30"><circle cx="15" cy="15" r="12" fill="none" stroke="var(--icon-fg)" stroke-width="2.5"/><path d="M17 6 L10 17 H15 L13 24 L20 13 H15 Z" fill="var(--icon-fg)"/></svg></div><div class="label" style="color:var(--orange)">ENERGY</div></div>
    <div class="abs pillar" style="left:430px"><div class="disc"><svg width="32" height="32" viewBox="0 0 32 32" fill="none" stroke="var(--icon-fg)" stroke-width="2.5"><path d="M8 4 v9 a7 7 0 0 0 14 0 V4"/><path d="M15 20 v3 a6 6 0 0 0 12 0 v-4"/><circle cx="27" cy="16" r="3"/></svg></div><div class="label" style="color:var(--grass)">WELLNESS</div></div>
    <div class="abs pillar" style="left:633px"><div class="disc"><svg width="34" height="20" viewBox="0 0 34 20" fill="var(--icon-fg)"><rect x="2" y="6" width="4" height="8"/><rect x="7" y="3" width="4" height="14"/><rect x="11" y="9" width="12" height="2"/><rect x="23" y="3" width="4" height="14"/><rect x="28" y="6" width="4" height="8"/></svg></div><div class="label" style="color:#666">EXERCISE</div></div>
    <div class="abs pillar" style="left:837px"><div class="disc"><svg width="30" height="32" viewBox="0 0 30 32"><path d="M15 3 a11 11 0 0 0 -11 11 c0 4 2 6 4 8 v7 h11 v-4 h4 a2 2 0 0 0 2 -2 v-4 h3 l-3 -6 a11 11 0 0 0 -10 -10z" fill="var(--icon-fg)"/></svg></div><div class="label" style="color:var(--sky)">MIND</div></div>
  </section>

  <div class="abs rule" style="left:11px;top:762px;width:980px"></div>

  <section class="mission">
    <div class="abs mission-photo" role="img" aria-label="Woman holding a brain model and a red heart"></div>
    <h2 class="abs mission-title">Our Mission</h2>
    <p class="abs mission-text">LumaCrest's mission is to help, educate, and inspire people to achieve optimal health and live fulfilled lives. LumaCrest encourages its members, both users and experts, to share their experiences so that people can receive the knowledge, support and inspiration to transform their lives!</p>
    <div class="abs vline" style="left:698px;top:801px;height:155px"></div>
    <div class="abs pill" style="top:801px;background:var(--orange-light)"><svg width="18" height="18" viewBox="0 0 18 18"><circle cx="9" cy="9" r="8" fill="#fff"/><path d="M7 5 L12 9 L7 13Z" fill="var(--orange-light)"/></svg>FUNCTIONAL MEDICINE</div>
    <div class="abs pill" style="top:854px;background:var(--orange-mid)"><svg width="18" height="18" viewBox="0 0 18 18"><circle cx="9" cy="9" r="8" fill="#fff"/><path d="M7 5 L12 9 L7 13Z" fill="var(--orange-mid)"/></svg>NUTRITION EXPERTS</div>
    <div class="abs pill" style="top:908px;background:var(--orange)"><svg width="18" height="18" viewBox="0 0 18 18"><circle cx="9" cy="9" r="8" fill="#fff"/><path d="M7 5 L12 9 L7 13Z" fill="var(--orange)"/></svg>THE COMMUNITY</div>
  </section>

  <div class="abs rule" style="left:11px;top:1001px;width:980px"></div>

  <section class="discussions">
    <h2 class="abs section-title">Join discussions&nbsp; - &nbsp;Find answers</h2>
    <div class="abs thumb" style="left:11px;top:1084px;background:linear-gradient(135deg,#cfe3ea,#e9ddc4)" role="img" aria-label="Senior couple smiling together"></div>
    <div class="abs caption" style="left:11px;top:1246px">Achieving Optimal Health</div>
    <div class="abs thumb" style="left:356px;top:1084px;background:linear-gradient(135deg,#d5d5d5,#8e8e8e)" role="img" aria-label="Man holding his aching lower back"></div>
    <div class="abs caption" style="left:356px;top:1246px">Overcoming Health Problems</div>
    <div class="abs thumb" style="left:11px;top:1325px;background:linear-gradient(135deg,#b9763c,#8a5228)" role="img" aria-label="Feet on a bathroom scale"></div>
    <div class="abs caption" style="left:11px;top:1487px">Reaching your Ideal Weight</div>
    <div class="abs thumb" style="left:356px;top:1325px;background:linear-gradient(135deg,#f2f0ec,#d8d2c8)" role="img" aria-label="Mother playing with her baby"></div>
    <div class="abs caption" style="left:356px;top:1487px">Pregnancy and Baby Health</div>

    <h3 class="abs cat-title">CATEGORIES</h3>
    <ul class="abs cats">
      <li class="current">Healthy Lifestyle</li><li>Health Problem</li><li>Weight Loss</li><li>Pregnancy</li><li>Female Health</li><li>Male Health</li><li>Child Health</li><li>Senior Health</li><li>Healthy Mind</li><li>Sports Nutrition</li>
    </ul>
  </section>

  <section class="abs testi">
    <h3 class="abs testi-title">TESTIMONIALS</h3>
    <div class="abs avatar" role="img" aria-label="Portrait of a member"></div>
    <p class="abs quote">“&nbsp;Nam a malesuada libero. Duis sodales et libero vel interdum. Interdum et malesuada fames ac ante ipsum primis in faucibus. Donec lobortis dui tortor, eu lobortis felis mattis nec. Sed justo quam, luctus eu mauris eget, euismod dapibus sem. Sed tempus feugiat ante, at ornare libero volutpat sed. Maecenas quis magna magna.&nbsp;”</p>
    <div class="abs author">Dana Reyes, NY</div>
  </section>

  <section class="abs signup">
    <h3 class="abs signup-title">TESTIMONIALS</h3>
    <div class="abs field" style="left:202px;width:202px">Name</div>
    <div class="abs field" style="left:413px;width:202px">Email ID</div>
    <div class="abs field" style="left:624px;width:254px">I am : ...a Health Professional
      <svg style="position:absolute;right:12px;top:13px" width="14" height="8" viewBox="0 0 14 8"><path d="M0 0 H14 L7 8Z" fill="#aaa"/></svg></div>
    <div class="abs btn">Signup Now</div>
  </section>

  <footer class="abs footer">
    <h4 class="abs f-head" style="left:14px">ABOUT US</h4>
    <p class="abs f-text" style="left:14px;top:78px;width:276px">Fusce ac urna ac mi tincidunt semper non at orci. Donec lacinia, nisi eu malesuada feugiat, sapien sapien tempor ante, sit amet dictum metus felis quis nibh. Fusce quis viverra mauris. Maecenas et augue commodo lorem consectetur suscipit.</p>
    <div class="abs f-more" style="left:14px;top:199px">MORE ›</div>
    <div class="abs f-div" style="left:315px"></div>
    <h4 class="abs f-head" style="left:348px">CONTACT US</h4>
    <p class="abs f-text" style="left:348px;top:78px;width:240px">55, Building name, Street name,<br>City- Zipcode<br>Call : 555 210 3348<br>Fax : 555 210 3348<br>E-mail : hello@lumacrest.com</p>
    <div class="abs f-more" style="left:348px;top:199px">VIEW MAP ›</div>
    <div class="abs f-div" style="left:594px"></div>
    <h4 class="abs f-head" style="left:625px">QUICK LINKS</h4>
    <ul class="abs f-links" style="left:625px"><li>Home</li><li>About us</li><li>Services</li><li>Testimonials</li><li>Media</li><li>Contact us</li></ul>
    <ul class="abs f-links" style="left:749px"><li>Healthy Lifestyle</li><li>Health Problem</li><li>Weight Loss</li><li>Pregnancy</li><li>Female Health</li><li>Male Health</li></ul>
    <ul class="abs f-links" style="left:895px"><li>Child Health</li><li>Senior Health</li><li>Healthy Mind</li><li>Sports Nutrition</li></ul>
  </footer>

  <div class="abs bottom">
    <div class="abs copy">Copyright &nbsp;©&nbsp; 2014 LumaCrest. &nbsp; All rights reserved.</div>
    <span class="abs social" style="left:662px" aria-label="Social link"></span>
    <span class="abs social" style="left:704px" aria-label="Social link"></span>
    <span class="abs social" style="left:746px" aria-label="Social link"></span>
    <span class="abs social" style="left:788px" aria-label="Social link"></span>
    <span class="abs social" style="left:830px" aria-label="Social link"></span>
    <span class="abs social" style="left:872px" aria-label="Social link"></span>
    <span class="abs social" style="left:914px" aria-label="Social link"></span>
    <span class="abs social" style="left:956px;display:flex;align-items:center;justify-content:center" aria-label="Email"><svg width="16" height="12" viewBox="0 0 16 12"><rect x="0.5" y="0.5" width="15" height="11" fill="none" stroke="#fff"/><path d="M0.5 0.5 L8 7 L15.5 0.5" fill="none" stroke="#fff"/></svg></span>
  </div>

</div>
</body>
</html>
```